Modern Lawfirm Business Card Design

We're looking for a business card to incorporate the newly created logo we had made.

Ideally looking for a law firm business card demonstrating, modern, minimalist, strong/bold design.

I'm open to any design honestly, but nothing "flashy".

Target Market(s)

Immigration law, family immigration, humanitarian, general legal

Industry/Entity Type

Law Firm

Contact Information for Business Card

Please use dummy information, name, street address, city, state, phone number, email, website.

Font styles to use
Serif
Sans Serif

Requirements
Must have
• Please use dummy information, name, street address, city, state, phone number, email, website.

```html
<!DOCTYPE html>
<html lang="en">
<head>
<meta charset="utf-8">
<title>Vanterra Immigration Law – Business Card</title>
<link href="https://fonts.googleapis.com/css2?family=Noto+Sans:wght@400;600&display=swap" rel="stylesheet">
<style>
  :root {
    --backdrop: #e8e4e4;
    --card-front: #f3f3f3;
    --card-back: #dadada;
    --brand-blue: #1f5a9c;
    --ink: #2a2a2a;
    --ink-soft: #3c3c3c;
  }
  * { margin: 0; padding: 0; box-sizing: border-box; }
  html, body {
    width: 984px; height: 1200px; overflow: hidden;
    background: var(--backdrop);
    font-family: "Noto Sans", Arial, sans-serif;
    color: var(--ink);
  }
  .card {
    position: absolute;
    width: 628px; height: 359px;
  }
  .card--front { left: 157px; top: 168px; background: var(--card-front); }
  .card--back  { left: 154px; top: 618px; background: var(--card-back); }

  .wordmark {
    display: flex; align-items: center; gap: 8px;
    color: var(--brand-blue);
    font-weight: 600;
    letter-spacing: 0.06em;
    text-transform: uppercase;
    line-height: 1.15;
  }
  .wordmark__square { background: var(--brand-blue); flex: none; }
  .wordmark__text { display: flex; flex-direction: column; }

  .card--front .wordmark { position: absolute; right: 40px; top: 60px; font-size: 18px; }
  .card--front .wordmark__square { width: 40px; height: 40px; }

  .card--back .wordmark {
    position: absolute; left: 0; right: 0; top: 146px;
    justify-content: center; font-size: 26px;
  }
  .card--back .wordmark__square { width: 58px; height: 58px; }

  .holder { position: absolute; left: 50px; top: 146px; }
  .holder__name { font-size: 23px; font-weight: 600; letter-spacing: 0.01em; line-height: 1.2; }
  .holder__role { font-size: 13.5px; color: var(--ink-soft); margin-top: 1px; }

  .address { position: absolute; left: 50px; top: 219px; font-size: 16.5px; line-height: 23px; color: var(--ink-soft); }

  .contact { position: absolute; left: 53px; top: 275px; list-style: none; font-size: 16.5px; color: var(--ink-soft); }
  .contact li { display: flex; align-items: center; gap: 9px; height: 28px; }
  .contact svg { width: 18px; height: 18px; fill: var(--brand-blue); }

  .website {
    position: absolute; left: 0; right: 0; top: 293px;
    text-align: center; font-size: 15px; letter-spacing: 0.12em; color: var(--ink-soft);
  }
</style>
</head>
<body>
  <section class="card card--front">
    <div class="wordmark">
      <span class="wordmark__square"></span>
      <span class="wordmark__text"><span>Vanterra</span><span>Immigration Law</span></span>
    </div>
    <div class="holder">
      <p class="holder__name">DANIEL MORENO</p>
      <p class="holder__role">Managing Director</p>
    </div>
    <p class="address">7788 Street Name Street Name<br>City Name</p>
    <ul class="contact">
      <li>
        <svg viewBox="0 0 24 24" aria-hidden="true"><path d="M6.6 10.8c1.4 2.8 3.8 5.1 6.6 6.6l2.2-2.2c.3-.3.7-.4 1-.2 1.1.4 2.3.6 3.6.6.6 0 1 .4 1 1V20c0 .6-.4 1-1 1C10.6 21 3 13.4 3 4c0-.6.4-1 1-1h3.5c.6 0 1 .4 1 1 0 1.3.2 2.5.6 3.6.1.3 0 .7-.2 1l-2.3 2.2z"/></svg>
        <span>000-111-22-333</span>
      </li>
      <li>
        <svg viewBox="0 0 24 24" aria-hidden="true"><path d="M2 5h20v14H2z M2 5l10 8 10-8" fill="var(--brand-blue)"/><path d="M3 6l9 7 9-7" fill="none" stroke="#f3f3f3" stroke-width="1.6"/></svg>
        <span>dmoreno@vanterra.com</span>
      </li>
    </ul>
  </section>

  <section class="card card--back">
    <div class="wordmark">
      <span class="wordmark__square"></span>
      <span class="wordmark__text"><span>Vanterra</span><span>Immigration Law</span></span>
    </div>
    <p class="website">www.vanterra.com</p>
  </section>
</body>
</html>
```